Business Card design needs editing

We have a business card design but I need to remove one of the providers. The provider to be removed is "Marlene Odgrave, Midwife.

Industry/Entity Type

Business

Contact Information for Business Card

I have uploaded a copy of our current business card

```html
<!DOCTYPE html>
<html lang="en">
<head>
<meta charset="utf-8">
<title>Cedar Grove Women's Care – Business Card</title>
<link rel="stylesheet" href="https://fonts.googleapis.com/css2?family=Lato:wght@400;700&family=Crimson+Text:wght@400&display=swap">
<style>
  :root {
    --backdrop: #e6e7e9;
    --card-white: #ffffff;
    --sky: #7dbccd;
    --sky-soft: #a9d6e2;
    --charcoal: #3a3b3d;
    --ink: #2a2b2d;
    --grey-text: #6e7073;
  }
  * { box-sizing: border-box; margin: 0; padding: 0; }
  html, body { width: 1200px; height: 873px; overflow: hidden; }
  body {
    background: var(--backdrop);
    display: flex;
    align-items: center;
    justify-content: center;
    gap: 44px;
    font-family: "Lato", sans-serif;
  }
  .card {
    position: relative;
    width: 520px;
    height: 297px;
    background: var(--card-white);
    border-radius: 16px;
    overflow: hidden;
    box-shadow: 0 6px 20px rgba(0,0,0,0.18);
  }
  .card-wave { position: absolute; inset: 0; width: 100%; height: 100%; }

  /* Front */
  .brand {
    position: absolute;
    left: 30px;
    top: 78px;
    display: flex;
    align-items: center;
    gap: 10px;
  }
  .brand-dot {
    width: 26px; height: 26px;
    border-radius: 50%;
    background: var(--sky);
    flex: none;
  }
  .brand-name {
    font-size: 11px;
    letter-spacing: 0.6px;
    text-transform: uppercase;
    color: var(--sky);
    line-height: 1.3;
  }
  .brand-field {
    font-size: 12px;
    color: var(--grey-text);
  }
  .providers {
    position: absolute;
    right: 26px;
    top: 82px;
    text-align: right;
    font-family: "Crimson Text", serif;
    font-size: 17px;
    line-height: 1.45;
    color: var(--ink);
    list-style: none;
  }
  .contact {
    position: absolute;
    left: 26px;
    bottom: 20px;
    font-style: normal;
    font-size: 12.5px;
    font-weight: 700;
    line-height: 1.45;
    color: var(--ink);
  }
  .contact-line { display: flex; align-items: center; gap: 6px; }
  .contact-line svg { width: 11px; height: 11px; fill: var(--ink); }

  /* Back */
  .back-brand {
    position: absolute;
    left: 0; right: 0;
    top: 96px;
    display: flex;
    align-items: center;
    justify-content: center;
    gap: 10px;
  }
  .back-brand .brand-dot { width: 34px; height: 34px; }
  .back-brand .brand-name { font-size: 17px; color: var(--charcoal); letter-spacing: 1px; }
  .web {
    position: absolute;
    left: 0; right: 0;
    top: 206px;
    text-align: center;
    font-size: 17px;
    letter-spacing: 1px;
    color: var(--ink);
  }
  .web-accent { position: absolute; }
</style>
</head>
<body>

<section class="card card-front" aria-label="Card front">
  <svg class="card-wave" viewBox="0 0 520 297" preserveAspectRatio="none" aria-hidden="true">
    <path d="M0,176 C140,162 240,136 300,88 C350,38 420,10 520,4 L520,297 L0,297 Z" fill="var(--sky)"/>
    <path d="M300,88 C350,38 420,10 520,4 L520,14 C430,20 360,50 312,92 Z" fill="var(--sky-soft)"/>
    <path d="M0,156 C110,150 200,136 262,108 C216,140 120,160 0,166 Z" fill="var(--charcoal)"/>
  </svg>

  <div class="brand">
    <span class="brand-dot"></span>
    <div>
      <div class="brand-name">Cedar Grove Women's Care</div>
      <div class="brand-field">Obstetrics &amp; Gynecology</div>
    </div>
  </div>

  <ul class="providers">
    <li>Jennifer Stuckey, MD</li>
    <li>Dana Whitfield, MD</li>
    <li>Laura Brennan, MD</li>
  </ul>

  <address class="contact">
    <div>418 Linden Ave. Ste 3B</div>
    <div>Dalton, GA 30720-4412</div>
    <div class="contact-line">
      <svg viewBox="0 0 24 24" aria-label="Phone"><path d="M6.6 10.8a15 15 0 0 0 6.6 6.6l2.2-2.2a1 1 0 0 1 1-.25 11.4 11.4 0 0 0 3.6.57 1 1 0 0 1 1 1V20a1 1 0 0 1-1 1A17 17 0 0 1 3 4a1 1 0 0 1 1-1h3.5a1 1 0 0 1 1 1c0 1.25.2 2.45.57 3.57a1 1 0 0 1-.25 1z"/></svg>
      555-210-4738
    </div>
    <div class="contact-line">
      <svg viewBox="0 0 24 24" aria-label="Fax"><path d="M6 2h10l2 2v5H6zM4 10h16a2 2 0 0 1 2 2v7H2v-7a2 2 0 0 1 2-2zm3 3v2h4v-2z"/></svg>
      555-210-4153
    </div>
    <div class="contact-line">
      <svg viewBox="0 0 24 24" aria-label="Website"><path d="M12 2a10 10 0 1 0 0 20 10 10 0 0 0 0-20zm0 2a8 8 0 0 1 0 16 8 8 0 0 1 0-16z"/></svg>
      www.cedargrovewc.com
    </div>
  </address>
</section>

<section class="card card-back" aria-label="Card back">
  <div class="back-brand">
    <span class="brand-dot"></span>
    <span class="brand-name">Cedar Grove Women's Care</span>
  </div>

  <svg class="web-accent" style="left:270px;top:178px" width="120" height="14" viewBox="0 0 120 14" aria-hidden="true">
    <path d="M0,14 L120,0 L118,6 L6,14 Z" fill="var(--sky)"/>
  </svg>
  <div class="web">www.cedargrovewc.com</div>
  <svg class="web-accent" style="left:120px;top:240px" width="130" height="14" viewBox="0 0 130 14" aria-hidden="true">
    <path d="M0,14 L124,0 L130,0 L128,6 Z" fill="var(--sky)"/>
  </svg>
</section>

</body>
</html>
```